Veteran owned/staffed Organization that hires Veterans into Ironworking

Please see attached documents for all details and info.
We want a tri-fold brochure to use as a recruiting tool.
Our slogan is:
"Revolutionizing the skilled workforce, one Veteran at a time"
Veteran Apprenticeship Program in Ironworking
Skills/Traits: Welding, bolting, rigging, connecting
Teamwork, camaraderie, GI Bill, Skilled Labor, Career, Community service
OJT, Apprenticeship, Career
Due to the large number of retirees from the baby boomer generation, ironworkers are in high demand. In Texas, the construction industry is on the rise and due to our training regiment, an average of 40 hrs/wk are worked. Our apprenticeship program follows the PLOWD curriculum and at the end of the 3-year course involving classroom learning, OJT and practical application the apprentice achieves journeymen status in ironworking. Journeyman status opens the door to possible postions like foremen, crane operators and project managers. Ironworkers perform their duties on steel structures that provide a skeleton for commercial buildings like hospitals, schools and skyscrapers. Some of the key skilled trades of ironworking are welding, rigging, bolting and connecting.
All Things Veterans
Camaraderie and Culture
-Veteran owned and majority staffed organization who are committed to the mission of providing opportunitites to Veterans
-Graduation celebration after completion of initial training period, holiday parties and get togethers at OKDs
-Work with other Veterans and always have your teammate’s six
-We’re building America, one Veteran career at a time
Professional Support
BRT is committed to providing Veterans with supportive services designed to assist you and your families in the following areas:
Financial, family and work-related support.
Community Service
Disaster Response
Louisiana Flooding - Sept 2016
As the 15th anniversery of 9/11 approached BRT worked to find a volunteer opportunity. An ambitious plan was formed to respond to the devastating 1000-year flood event in Baton Rouge. With little time for planning, BRT organized all the tools and supplies necessary to take 24 Veterans to assist a community in extreme poverty. The team gutted the homes of nine residents which included: single mothers, handicapped elderaly and a Korean War Veterans
Hurricane Matthew - Oct 2016
In a period of 24 hours BRT mobilized 16 Veterans with the supplies neccessary to be 100% self-reliant. The team arrived in Holly Hill, SC 8 hours after Hurrican Matthew made landfall. During a period of 2 days, BRT provided over 5,000 meals, distributed 40,000 bottles of water and removed nearly 100 trees.

Target Market(s)

Veterans who are interested in becoming Ironworkers. Usually under the age of 40, have served in the military and are in the Texas area.

Industry/Entity Type

Construction

Font styles to use
Other font styles liked:
• Microgramma in some places (Logo font) and Serif type font for the bulk

Requirements
Must have
• The colors and logo mentioned in the template guidelines document.
• The slogan
• "Revolutionizing the skilled workforce, one Veteran at a time"
Nice to have
• Some charts and graphs if possible?

```html
<!DOCTYPE html>
<html lang="en">
<head>
<meta charset="utf-8">
<title>BRT Veteran Ironworking Tri-fold Brochure</title>
<link href="https://fonts.googleapis.com/css2?family=Michroma&family=Questrial&display=swap" rel="stylesheet">
<style>
  :root{
    --navy:#1d3550;
    --navy-deep:#142840;
    --gold:#e2a447;
    --gold-light:#f6c777;
    --gold-dark:#b47a33;
    --frame:#c38a3d;
    --ink:#27405c;
    --body:#585858;
    --paper:#ffffff;
    --stage:#e4e4e4;
  }
  *{box-sizing:border-box;margin:0;padding:0}
  html,body{width:1200px;height:800px;overflow:hidden;background:var(--stage)}
  .canvas{position:relative;width:1200px;height:800px}
  .brochure{position:absolute;left:45px;width:1110px;height:365px;overflow:hidden;box-shadow:0 6px 18px rgba(0,0,0,.18)}
  .brochure--inside{top:20px;background:var(--paper)}
  .brochure--outside{top:412px;background:var(--navy)}
  .brochure__art{position:absolute;inset:0}
  .panel{position:absolute;top:0;width:370px;height:365px}
  .panel--1{left:0}.panel--2{left:370px}.panel--3{left:740px}
  .heading{font-family:"Michroma",sans-serif;color:var(--ink);font-size:11.5px;letter-spacing:.2px}
  .copy{font-family:"Questrial",sans-serif;color:var(--body);font-size:8.2px;line-height:11px}
  .copy p{margin-bottom:4px}
  .subhead{font-family:"Questrial",sans-serif;color:var(--ink);font-size:8.6px;font-weight:bold}

  /* inside */
  .career .heading{position:absolute;left:26px;top:22px}
  .career .copy{position:absolute;left:26px;top:46px;width:320px}
  .veterans .heading{position:absolute;left:24px;top:22px}
  .veterans .bullets{position:absolute;left:24px;top:46px;width:320px;list-style:none}
  .veterans .bullets li{position:relative;padding-left:13px;margin-bottom:7px}
  .veterans .bullets li::before{content:"";position:absolute;left:0;top:3px;width:6px;height:6px;border-radius:50%;background:var(--gold)}
  .community .heading{position:absolute;left:22px;top:22px}
  .community .copy{position:absolute;left:22px;top:44px;width:240px}
  .community .copy.wide{top:122px;width:326px}
  .program-band{position:absolute;left:470px;top:306px;width:630px}
  .program-band .title{font-family:"Michroma",sans-serif;font-size:12.5px;color:var(--navy)}
  .program-band .line{font-family:"Michroma",sans-serif;font-size:9px;color:var(--navy);margin-top:4px}

  /* outside */
  .about .heading{position:absolute;left:26px;top:30px;color:#fff;font-size:13px}
  .about .copy{position:absolute;left:26px;top:56px;width:318px;color:#fff;font-size:8.6px;line-height:11.5px}
  .contact{position:absolute;left:0;top:60px;width:370px;text-align:center}
  .brand-name{font-family:"Michroma",sans-serif;color:var(--gold);letter-spacing:2px}
  .contact .brand-name{font-size:18px;color:#fff}
  .contact .brand-sub{font-family:"Michroma",sans-serif;font-size:5.5px;color:#fff;letter-spacing:1px;margin-top:2px}
  .contact .lines{font-family:"Michroma",sans-serif;font-size:9px;color:#fff;line-height:14px;margin-top:12px}
  .cover-mark{position:absolute;left:0;top:28px;width:370px;text-align:center}
  .cover-mark .brand-name{font-size:30px}
  .cover-mark .brand-sub{font-family:"Michroma",sans-serif;font-size:6.5px;color:var(--gold);letter-spacing:1.5px;margin-top:4px}
</style>
</head>
<body>
<div class="canvas">

  <section class="brochure brochure--inside" aria-label="Brochure inside spread">
    <svg class="brochure__art" width="1110" height="365" viewBox="0 0 1110 365">
      <defs>
        <linearGradient id="goldBand" x1="0" y1="0" x2="1" y2="0">
          <stop offset="0" stop-color="#f0b85c"/><stop offset="1" stop-color="#f8cf86"/>
        </linearGradient>
        <linearGradient id="steelSky" x1="0" y1="0" x2="0" y2="1">
          <stop offset="0" stop-color="#5f7fae"/><stop offset="1" stop-color="#a9b8c9"/>
        </linearGradient>
        <linearGradient id="sitePhoto" x1="0" y1="0" x2="1" y2="1">
          <stop offset="0" stop-color="#6f86a8"/><stop offset="1" stop-color="#7a5e48"/>
        </linearGradient>
      </defs>
      <path d="M0 0 H370 V10 Q180 8 0 40 Z" fill="url(#goldBand)" opacity=".9"/>
      <rect x="0" y="352" width="370" height="13" fill="url(#goldBand)"/>
      <path role="img" aria-label="Photo of ironworkers on a steel frame against the sky" d="M470 250 H1110 V365 H430 Z" fill="url(#steelSky)"/>
      <path d="M380 365 L440 292 Q760 300 1110 285 V365 Z" fill="url(#goldBand)"/>
      <polygon role="img" aria-label="Photo of a steel beam structure" points="135,305 107.5,352.6 52.5,352.6 25,305 52.5,257.4 107.5,257.4" fill="url(#steelSky)" stroke="var(--frame)" stroke-width="6"/>
      <polygon role="img" aria-label="Photo of steel framing from below" points="220,240 200,274.6 160,274.6 140,240 160,205.4 200,205.4" fill="url(#sitePhoto)" stroke="var(--frame)" stroke-width="5"/>
      <polygon role="img" aria-label="Photo of a crew of Veterans at work" points="263,322 244,354.9 206,354.9 187,322 206,289.1 244,289.1" fill="#8c6a52" stroke="var(--frame)" stroke-width="5"/>
      <polygon role="img" aria-label="Photo of an ironworker tying in on a site" points="503,225 479,266.6 431,266.6 407,225 431,183.4 479,183.4" fill="url(#sitePhoto)" stroke="var(--frame)" stroke-width="6"/>
      <polygon role="img" aria-label="Photo of a Veteran volunteer in a hard hat" points="1100,55 1077.5,94 1032.5,94 1010,55 1032.5,16 1077.5,16" fill="#6d7f98" stroke="var(--frame)" stroke-width="6"/>
      <line x1="370" y1="0" x2="370" y2="365" stroke="#000" stroke-opacity=".06"/>
      <line x1="740" y1="0" x2="740" y2="365" stroke="#000" stroke-opacity=".06"/>
    </svg>

    <div class="panel panel--1 career">
      <h2 class="heading">OJT, Apprenticeship and Career</h2>
      <div class="copy">
        <p>Due to the large number of retirees from the baby boomer generation, ironworkers are in high demand. In Texas, the construction industry is on the rise and due to our training regiment, an average of 40 hrs/wk are worked.</p>
        <p>Our apprenticeship program follows the PLOWD curriculum and at the end of the 3-year course involving classroom learning, OJT and practical application the apprentice achieves journeymen status in ironworking. Journeyman status opens the door to possible positions like foremen, crane operators and project managers.</p>
        <p>Ironworkers perform their duties on steel structures that provide a skeleton for commercial buildings like hospitals, schools and skyscrapers. Some of the key skilled trades of ironworking are welding, rigging, bolting and connecting.</p>
      </div>
    </div>

    <div class="panel panel--2 veterans">
      <h2 class="heading">All Things Veterans</h2>
      <ul class="bullets copy">
        <li>Veteran owned and majority staffed organization who are committed to the mission of providing opportunities to Veterans</li>
        <li>Graduation celebrations after completion of initial training period, holiday parties and get-togethers at OKDs</li>
        <li>We have partnered and participate with a variety of Veteran Service Organizations to provide networking events, Veteran support and camaraderie</li>
        <li>Work with other Veterans and always have your teammate's six</li>
      </ul>
    </div>

    <div class="panel panel--3 community">
      <h2 class="heading">Community Service</h2>
      <div class="copy">
        <p class="subhead">Disaster Response</p>
        <p class="subhead">Louisiana Flooding - Sept 2016</p>
        <p>As the 15th anniversary of 9/11 approached BRT worked to find a volunteer opportunity. An ambitious plan was formed to respond to the devastating 1000-year flood event in Baton Rouge.</p>
      </div>
      <div class="copy wide">
        <p>With little time for planning, BRT organized all the tools and supplies necessary to take 24 Veterans to assist a community in extreme poverty. The team gutted the homes of nine residents which included single mothers, handicapped elderly and a Korean War Veteran.</p>
        <p class="subhead">Hurricane Matthew - Oct 2016</p>
        <p>In a period of 24 hours BRT mobilized 16 Veterans with the supplies necessary to be 100% self-reliant. The team arrived in Holly Hill, SC 8 hours after Hurricane Matthew made landfall. During a period of 2 days, BRT provided over 5,000 meals, distributed 40,000 bottles of water and removed nearly 100 trees.</p>
      </div>
    </div>

    <div class="program-band">
      <div class="title">Veteran Apprenticeship Program in Ironworking</div>
      <div class="line">Skills/Traits: Welding, bolting, rigging, connecting</div>
      <div class="line">Teamwork, camaraderie, GI Bill, Skilled Labor, Career, Community service</div>
    </div>
  </section>

  <section class="brochure brochure--outside" aria-label="Brochure outside spread">
    <svg class="brochure__art" width="1110" height="365" viewBox="0 0 1110 365">
      <defs>
        <linearGradient id="aboutGold" x1="0" y1="0" x2="1" y2="1">
          <stop offset="0" stop-color="#e9b25c"/><stop offset=".55" stop-color="#c98d3e"/><stop offset="1" stop-color="#a26a2a"/>
        </linearGradient>
        <linearGradient id="hatPhoto" x1="0" y1="0" x2="1" y2="1">
          <stop offset="0" stop-color="#8a9a86"/><stop offset=".5" stop-color="#3f8a55"/><stop offset="1" stop-color="#7e6e70"/>
        </linearGradient>
        <linearGradient id="monoPhoto" x1="0" y1="0" x2="1" y2="1">
          <stop offset="0" stop-color="#9a9a9a"/><stop offset="1" stop-color="#5d5d5d"/>
        </linearGradient>
        <linearGradient id="sloganBand" x1="0" y1="0" x2="1" y2="0">
          <stop offset="0" stop-color="#e7a94f"/><stop offset="1" stop-color="#f8d08a"/>
        </linearGradient>
        <linearGradient id="hexPhoto" x1="0" y1="0" x2="1" y2="1">
          <stop offset="0" stop-color="#6f7f96"/><stop offset="1" stop-color="#8b5a3c"/>
        </linearGradient>
      </defs>
      <rect x="0" y="0" width="372" height="365" fill="url(#aboutGold)"/>
      <path role="img" aria-label="Photo of a Veteran ironworker in a green hard hat" d="M370 365 V215 Q520 175 740 200 V365 Z" fill="url(#hatPhoto)"/>
      <path d="M370 0 H420 Q395 120 372 365 H370 Z" fill="var(--gold-dark)" opacity=".8"/>
      <path role="img" aria-label="Black and white photo of a crew on a building site" d="M740 130 Q900 110 1110 80 V365 H740 Z" fill="url(#monoPhoto)"/>
      <!-- slogan band -->
      <polygon class="slogan-band" points="790,365 1110,215 1110,290 950,365" fill="url(#sloganBand)"/>
      <text class="slogan" transform="translate(1010,299) rotate(-25)" text-anchor="middle" font-family="Michroma, sans-serif" font-size="9" fill="#1d3550">
        <tspan x="0" dy="-9">"Revolutionizing</tspan>
        <tspan x="0" dy="13">the skilled workforce,</tspan>
        <tspan x="0" dy="13">one Veteran at a time"</tspan>
      </text>
      <!-- support cube -->
      <polygon points="175,172 240,198 175,224 110,198" fill="#f3c06d" stroke="#fff" stroke-width="1"/>
      <polygon points="110,198 175,224 175,292 110,266" fill="var(--navy)" stroke="#fff" stroke-width="1"/>
      <polygon points="175,224 240,198 240,266 175,292" fill="#e9ad55" stroke="#fff" stroke-width="1"/>
      <g font-family="Michroma, sans-serif" font-size="7" text-anchor="middle">
        <text x="175" y="202" fill="#1d3550">Family Support</text>
        <text x="142" y="248" fill="#fff">Financial</text><text x="142" y="258" fill="#fff">Support</text>
        <text x="208" y="248" fill="#1d3550">Workplace</text><text x="208" y="258" fill="#1d3550">Support</text>
      </g>
      <polygon role="img" aria-label="Photo of a welder at work" points="97,320 76,356.4 34,356.4 13,320 34,283.6 76,283.6" fill="url(#hexPhoto)" stroke="var(--frame)" stroke-width="5"/>
      <polygon role="img" aria-label="Photo of a steel column against the sky" points="330,320 310,354.6 270,354.6 250,320 270,285.4 310,285.4" fill="#7e93b0" stroke="var(--frame)" stroke-width="5"/>
      <line x1="740" y1="0" x2="740" y2="365" stroke="#000" stroke-opacity=".12"/>
    </svg>

    <div class="panel panel--1 about">
      <h2 class="heading">ABOUT US</h2>
      <div class="copy">
        <p>Bold Ridge Trades partners with employers to develop skilled ironworkers from qualified U.S. Military Veterans at no cost to the Veteran. Veterans are employed, trained and join companies and crews with other Veterans.</p>
        <p>BRT is committed to providing Veterans with supportive services designed to assist you and your families in the following areas:</p>
      </div>
    </div>

    <div class="panel panel--2">
      <div class="contact">
        <div class="brand-name">BRT</div>
        <div class="brand-sub">BOLD RIDGE TRADES</div>
        <div class="lines">
          <div>BRTTexas</div>
          <div>www.BRTTexas.com</div>
          <div>Recruiting@BRTTexas.com</div>
        </div>
      </div>
    </div>

    <div class="panel panel--3">
      <div class="cover-mark">
        <div class="brand-name">BRT</div>
        <div class="brand-sub">BOLD RIDGE TRADES</div>
      </div>
    </div>
  </section>

</div>
</body>
</html>
```